Design A Dog Teeth Cleaning Certificate

Hello,
I need a Dog Teeth Cleaning Certificate made to fit on a standard tavlo display. I will provide exact dimensions at a later time. Now please design for tavlo.

Theme and artwork should match our brand and current logo. See attached word document for kelvane link and further details.

Certificate would be given to all Pet Parents who have their pets teeth cleaned without Anesthesia as a certificate of completion.

I would like you to be creative and come up with something fun.

Examples: https://www.quarnfeld.example/find?q=Certificate+for+teeth+cleaning&client=brisk-a&hs=Q7M&rls=org.velmont:en-US:official&source=pqrs&tbm=img&sa=Y&ei=kp4DTvm2HcddzRJ2-ZEZDx&ved=1DBlR_BVpBQ&biw=1411&bih=718

Please allow a place for Pet Parent name and Pets name.

```html
<!DOCTYPE html>
<html lang="en">
<head>
<meta charset="utf-8">
<title>Dog Teeth Cleaning Certificate</title>
<link rel="stylesheet" href="https://fonts.googleapis.com/css2?family=Josefin+Sans:wght@400;600;700&family=Lobster&display=swap">
<style>
  :root {
    --page-bg: #d9d9d7;
    --frame-dark: #7a5a12;
    --frame-mid: #c9a13a;
    --frame-light: #f3d77a;
    --paper: #fbf7ec;
    --gold-text: #c49a3c;
    --gold-soft: #e2cf9e;
    --red: #c8151b;
    --ink: #1d1d1d;
    --muted: #6b6b6b;
    --line: #8d8d8d;
  }
  * { margin: 0; padding: 0; box-sizing: border-box; }
  html, body { width: 1200px; height: 803px; overflow: hidden; background: var(--page-bg); }
  .certificate {
    position: relative;
    width: 1200px; height: 803px;
    padding: 38px;
    background: linear-gradient(135deg, var(--frame-light), var(--frame-mid) 30%, var(--frame-dark) 55%, var(--frame-mid) 75%, var(--frame-light));
  }
  .certificate__paper {
    position: relative;
    width: 100%; height: 100%;
    background: var(--paper);
    border: 6px solid var(--frame-dark);
    box-shadow: inset 0 0 0 3px var(--frame-light);
    font-family: "Josefin Sans", sans-serif;
    color: var(--ink);
    overflow: hidden;
  }
  .title {
    position: absolute; left: 70px; top: 50px; width: 600px;
    text-align: center;
    font-weight: 700; font-size: 48px; line-height: 1.05;
    color: var(--gold-text);
    letter-spacing: 1px;
  }
  .title__rule { position: absolute; left: 150px; top: 170px; }
  .paw {
    position: absolute; width: 46px; height: 46px; border-radius: 10px;
    background: linear-gradient(160deg, var(--gold-soft), var(--gold-text));
  }
  .paw--left { left: 80px; top: 170px; }
  .paw--right { left: 690px; top: 74px; }
  .brand {
    position: absolute; right: 50px; top: 40px;
    display: flex; align-items: center; gap: 12px;
    font-weight: 700; font-size: 26px; color: var(--red);
  }
  .brand__dot { width: 26px; height: 26px; border-radius: 50%; background: var(--red); }
  .headline {
    position: absolute; left: 0; right: 0; top: 200px;
    text-align: center;
    font-family: "Lobster", cursive; font-weight: 400; font-size: 130px; line-height: 1;
    color: var(--red);
  }
  .body-text { position: absolute; left: 90px; top: 380px; }
  .body-text p { font-size: 28px; font-weight: 600; line-height: 1.4; }
  .blank { display: inline-block; width: 300px; border-bottom: 2px solid var(--ink); margin-left: 10px; }
  .body-text .course { margin-top: 4px; color: var(--gold-text); font-weight: 700; letter-spacing: 2px; }
  .signature { position: absolute; width: 220px; text-align: center; font-size: 20px; color: var(--muted); }
  .signature::before { content: ""; display: block; width: 200px; height: 2px; background: var(--line); margin: 0 auto 8px; }
  .signature--vet { right: 60px; top: 470px; }
  .signature--parent { left: 500px; top: 600px; }
  .seal {
    position: absolute; left: 95px; top: 565px; width: 110px; height: 110px; border-radius: 50%;
    background: radial-gradient(circle, var(--red) 0 55%, var(--gold-text) 57% 100%);
  }
  .seal__date { position: absolute; left: 90px; top: 688px; width: 120px; text-align: center; font-size: 20px; color: var(--muted); }
</style>
</head>
<body>
  <main class="certificate">
    <section class="certificate__paper">
      <span class="paw paw--left" role="img" aria-label="Gold paw print"></span>
      <span class="paw paw--right" role="img" aria-label="Gold paw print"></span>

      <h1 class="title">DOG TEETH CLEANING<br>CERTIFICATE</h1>
      <svg class="title__rule" width="440" height="16" viewBox="0 0 440 16" aria-hidden="true">
        <path d="M0 8 L420 4 L440 8 L420 12 Z" fill="#c49a3c"/>
      </svg>

      <div class="brand"><span class="brand__dot"></span>Bramble Smiles</div>

      <h2 class="headline">Congratulation!</h2>

      <div class="body-text">
        <p>Let it be know that <span class="blank"></span></p>
        <p>Has sucessfully participated to the clinic entitled</p>
        <p class="course">CLEANING TEETH WITHOUT ANESTHESIA</p>
      </div>

      <div class="signature signature--vet">Veterinary Surgeon</div>
      <div class="signature signature--parent">Pet's parents</div>

      <div class="seal" role="img" aria-label="2014 award seal with red ribbon"></div>
      <div class="seal__date">Jan - 2014</div>
    </section>
  </main>
</body>
</html>
```